Website Design for Varnel Ridge Holdings

I am looking to create a website with 3-4 pages for Varnel Ridge Holdings, a private investment holding company. We already have a logo created via PixelHarbor and would like to incorporate the same dark navy blue color scheme as well as white and potentially other colors including variants of blue, black, and white. We are looking for a conservative, polished design befitting a financial services firm. Our focus as a firm is on identifying opportunities in the overlooked - seeing opportunity where institutional investment is lacking. We are focused on building value for the long-term. We will provide virtually all of the text content but need assistance in setting up the layout, font, design, theme, graphics, etc. The initial three pages will be: Home Page / About Us, "Team", and "Portfolio". Right now, we do not have any portfolio companies but will likely have one within the next several months. The main content page will be the home page. The Team and Portfolio pages will be abbreviated. This website will be expository and is not primarily focused on lead generation or sales.

Ideally, we can incorporate some form of animations / transitions for titles and text sections and stock images (or ideally looped videos) of major city skylines in the U.S. , Latin America, and Europe as those regions are our core investment geographies.

Websites we like that you can use for references include many major private equity firms including Quarrystone Partners (https://www.quarrystonepartners.example/), Brightmoor (https://brightmoor.example/), KLV Holdings (https://www.klvholdings.example/), and Wexholm (https://www.wexholm.example/)
Updates

All,

Thank you to everyone who has posted the initial drafts of the Varnel Ridge Holdings website. The designs are very good. We would now like to review more refined drafts of our website from the designers.

We have posted updated, specific guidance on website page design and text. Please reference the new uploaded "Varnel Ridge Holdings Website Design Guidance" Microsoft Word document to refine your submissions.

Thank you!
Marcus

Target Market(s)

Investment Professionals

Industry/Entity Type

Financial Services

Coding

Coded - Design and coding required

Number of Pages Required

4 page

```html
<!DOCTYPE html>
<html lang="en">
<head>
<meta charset="utf-8">
<title>Varnel Ridge Holdings</title>
<link rel="stylesheet" href="https://fonts.googleapis.com/css2?family=Poppins:wght@300;400;500;600;700;800&display=swap">
<style>
:root{
  --navy:#0c1e45;
  --navy-deep:#081738;
  --ink:#0f1d3d;
  --text:#4a4f5c;
  --muted:#8a8f9a;
  --pale:#f0f2f6;
  --white:#ffffff;
}
*{margin:0;padding:0;box-sizing:border-box}
html,body{width:1200px;height:4992px;overflow:hidden}
body{font-family:"Poppins",sans-serif;color:var(--text);background:var(--white);position:relative}
.abs{position:absolute}
.photo{position:absolute}
a{color:inherit;text-decoration:none}

/* utility bar */
.utility-bar{position:absolute;left:0;top:0;width:1200px;height:42px;background:var(--navy)}
.utility-bar a{position:absolute;top:13px;font-size:10.5px;font-weight:500;letter-spacing:.5px;color:#aab3c8}

/* hero */
.hero{position:absolute;left:0;top:42px;width:1200px;height:608px;background:linear-gradient(180deg,#5a6b80 0%,#44515f 40%,#3a4048 75%,#6b7a72 100%)}
.hero-shade{position:absolute;inset:0;background:linear-gradient(90deg,rgba(50,90,110,.35),rgba(20,30,45,.1) 50%,rgba(30,35,45,.2))}
.site-nav{position:absolute;left:128px;top:68px;width:944px;height:72px;background:var(--white);border-radius:12px}
.brand{position:absolute;left:18px;top:22px;font-size:22px;font-weight:600;letter-spacing:1.5px;color:var(--navy);white-space:nowrap}
.site-nav a{position:absolute;top:28px;font-size:13px;font-weight:500;color:var(--ink)}
.hero-title{position:absolute;left:0;top:262px;width:1200px;text-align:center;font-size:50px;line-height:58px;font-weight:700;color:var(--white);text-transform:uppercase;letter-spacing:-.5px}
.hero-btn{position:absolute;left:498px;top:401px;width:204px;height:51px;background:var(--navy);border:2px solid var(--white);color:var(--white);font-size:16px;font-weight:700;text-align:center;line-height:47px}

/* about */
.eyebrow{font-size:15px;font-weight:600;color:var(--muted);text-transform:uppercase;letter-spacing:.3px}
.section-heading{font-size:30px;line-height:34px;font-weight:700;color:var(--ink)}
.body-copy{font-size:13.5px;line-height:24px;color:var(--text)}
.accent-bar{position:absolute;background:var(--navy)}

/* stats */
.stat{position:absolute;width:300px;text-align:center}
.stat-value{font-size:86px;line-height:90px;font-weight:300;color:var(--ink);letter-spacing:-1px}
.stat-label{font-size:15px;color:var(--ink);margin-top:6px}

/* services */
.services{position:absolute;left:0;top:1429px;width:1200px;height:659px;background:var(--pale)}
.center-heading{position:absolute;left:0;width:1200px;text-align:center;font-size:28px;font-weight:700;color:var(--ink)}
.center-copy{position:absolute;left:0;width:1200px;text-align:center;font-size:13.5px;line-height:22px;color:var(--text)}
.service-card{position:absolute;top:219px;width:260px;height:322px;background:var(--white);box-shadow:0 4px 16px rgba(12,30,69,.08)}
.service-card svg{position:absolute;left:32px;top:50px}
.service-title{position:absolute;left:32px;top:146px;font-size:18px;line-height:27px;font-weight:600;color:var(--ink)}
.service-copy{position:absolute;left:32px;top:210px;width:210px;font-size:13.5px;line-height:20px;color:var(--muted)}

/* partner */
.quote-copy{position:absolute;left:128px;top:2410px;width:420px;padding-left:22px;border-left:2px solid var(--navy)}
.outline-btn{position:absolute;left:128px;top:2567px;width:126px;height:43px;border:2px solid var(--ink);font-size:14px;font-weight:700;color:var(--ink);text-align:center;line-height:39px}

/* team band */
.team-band{position:absolute;left:0;top:2786px;width:1200px;height:486px;background:linear-gradient(90deg,#233a60,#2e4468 45%,#1e3358)}
.team-band::after{content:"";position:absolute;inset:0;background:rgba(12,30,69,.55)}
.team-band h2{position:absolute;z-index:1;left:0;top:3020px;width:1200px}

/* news */
.news{position:absolute;left:0;top:3937px;width:1200px;height:683px;background:var(--pale)}
.news-card{position:absolute;top:179px;width:294px}
.news-card .photo{position:relative;width:294px;height:225px}
.news-title{margin-top:34px;font-size:19px;line-height:25px;font-weight:700;color:var(--ink)}
.news-copy{margin-top:16px;font-size:13.5px;line-height:21px;color:var(--text)}

/* footer */
.site-footer{position:absolute;left:0;top:4620px;width:1200px;height:372px;background:var(--navy)}
.footer-brand{position:absolute;left:128px;top:80px;font-size:32px;font-weight:600;letter-spacing:2px;color:var(--white);white-space:nowrap}
.footer-copy{position:absolute;left:128px;top:150px;width:420px;font-size:13.5px;line-height:24px;color:#d4d9e4}
.footer-links{position:absolute;top:64px;list-style:none}
.footer-links li{font-size:12.5px;font-weight:500;color:#d4d9e4;line-height:30px;text-transform:uppercase}
.footer-rule{position:absolute;left:128px;top:296px;width:944px;height:1px;background:#3a4a70}
.copyright{position:absolute;left:128px;top:328px;font-size:14px;color:#c2c9d8}
.social-dot{position:absolute;left:1050px;top:328px;width:20px;height:20px;border-radius:50%;background:#8a95ad}
</style>
</head>
<body>

<div class="utility-bar">
  <a style="left:872px">SEARCH</a>
  <a style="left:957px">INVESTOR PORTAL</a>
</div>

<section class="hero" role="img" aria-label="City skyline along a lakefront under a grey sky">
  <div class="hero-shade"></div>
</section>
<nav class="site-nav">
  <span class="brand">VARNEL RIDGE HOLDINGS</span>
  <a style="left:417px">HOME</a>
  <a style="left:484px">ABOUT US</a>
  <a style="left:601px">TEAM</a>
  <a style="left:683px">PORTFOLIO</a>
  <a style="left:806px">CONTACT US</a>
</nav>
<h1 class="hero-title">Welcome to Varnel Ridge<br>Holdings</h1>
<a class="hero-btn">CONTACT US</a>

<!-- about -->
<div class="accent-bar" style="left:533px;top:770px;width:23px;height:201px"></div>
<div class="photo" style="left:128px;top:731px;width:423px;height:421px;background:linear-gradient(135deg,#6c7680 0%,#9aa0a4 35%,#d7a58c 60%,#3a3f4a 100%)" role="img" aria-label="Two business people shaking hands in an office"></div>
<div class="accent-bar" style="left:109px;top:1030px;width:38px;height:133px"></div>
<div class="abs eyebrow" style="left:611px;top:775px">Who We Are</div>
<h2 class="abs section-heading" style="left:611px;top:804px;width:460px;text-transform:uppercase">About Varnel Ridge Holdings</h2>
<p class="abs body-copy" style="left:611px;top:889px;width:455px">Lorem ipsum dolor sit amet, consectetur adipiscing elit sed do eiusmod tempor incididunt ut labore et dolorem agna aliqua. Quis ipsum suspendisse ultrices gravidaisus commodo vive rra maecenas accumsaLorem ipsum dolor sit amet, consloree ctetur adipiscing elit, sed do eiusmod tempor incididuno vive rra maecenas accumsaLorem ipum dolor sit amet, consloree ctetur adipiscing elit, sed do eiuod tempor incididuntt lorut labore et dolore magna aliqs ips um suspendisse.</p>

<div class="stat" style="left:137px;top:1242px"><div class="stat-value">30+</div><div class="stat-label">Years in Business</div></div>
<div class="stat" style="left:418px;top:1242px"><div class="stat-value">500+</div><div class="stat-label">Acquisitions to Date</div></div>
<div class="stat" style="left:732px;top:1242px"><div class="stat-value">50M</div><div class="stat-label">Assets Under Management</div></div>

<!-- services -->
<section class="services">
  <h2 class="center-heading" style="top:82px">WHAT WE DO</h2>
  <p class="center-copy" style="top:130px">Lorem ipsum dolor sit amet, consectetur adipiscing elit, sed do eiusmod tem<br>por incididunt ut labore et dolore magna aliquauis ipsum suspendiss.</p>

  <div class="service-card" style="left:182px">
    <svg width="64" height="64" viewBox="0 0 64 64" fill="none" stroke="#0c1e45" stroke-width="3.5" stroke-linecap="round" stroke-linejoin="round">
      <path d="M4 34 L18 20 L28 28 L44 10"/><path d="M36 10 H44 V18"/>
      <path d="M8 58 V46 M18 58 V40 M28 58 V44"/>
      <path d="M54 30 V60 M60 36 C60 32 48 32 48 38 C48 44 60 42 60 49 C60 55 48 55 48 51"/>
    </svg>
    <div class="service-title">Middle Market<br>Private Equity</div>
    <div class="service-copy">Lorem ipsum dolor sitame conse ctetur adipiscing eli ed do eiusmod.</div>
  </div>

  <div class="service-card" style="left:469px">
    <svg width="64" height="64" viewBox="0 0 64 64" fill="none" stroke="#0c1e45" stroke-width="3.5" stroke-linecap="round" stroke-linejoin="round">
      <path d="M22 14 V8 H38 V14"/><path d="M30 54 H8 C5 54 4 52 4 50 V18 C4 16 5 14 8 14 H52 C55 14 56 16 56 18 V30"/>
      <path d="M4 30 H30"/><circle cx="46" cy="46" r="13"/><path d="M46 39 V46 L51 50"/>
    </svg>
    <div class="service-title">Small Business<br>Private Equity</div>
    <div class="service-copy">Lorem ipsum dolor sitame conse ctetur adipiscing eli ed do eiusmod.</div>
  </div>

  <div class="service-card" style="left:760px">
    <svg width="64" height="64" viewBox="0 0 64 64" fill="none" stroke="#0c1e45" stroke-width="3.5" stroke-linecap="round" stroke-linejoin="round">
      <circle cx="16" cy="12" r="8"/><path d="M4 34 C4 26 9 22 16 22 C23 22 28 26 28 34"/>
      <path d="M30 30 L56 6"/><path d="M48 6 H56 V14"/>
      <path d="M22 60 V50 M32 60 V44 M42 60 V36 M52 60 V28"/>
    </svg>
    <div class="service-title" style="top:160px">Growth Capital</div>
    <div class="service-copy">Lorem ipsum dolor sitame conse ctetur adipiscing eli ed do eiusmod.</div>
  </div>
</section>

<!-- partner -->
<div class="abs eyebrow" style="left:128px;top:2258px">Who We Are</div>
<h2 class="abs section-heading" style="left:128px;top:2304px;width:460px">A Trusted, Value-Added<br>Partner for Your Business</h2>
<p class="quote-copy body-copy">Lorem ipsum dolor sit amet, consectetur adipiscing elit, sed do eiusmod tempor incididunt ut labore et dolore magna aliqua. Quis ipsum suspendisse ultrices gravida. Risus commodo viverra maecenas accumsan lacus vel facilisis.</p>
<a class="outline-btn">READ MORE</a>
<div class="photo" style="left:626px;top:2243px;width:304px;height:366px;background:linear-gradient(135deg,#c9a98a 0%,#8a7d74 40%,#2f3a4e 75%,#dcdcdc 100%)" role="img" aria-label="Smiling businessman in a suit talking with a colleague"></div>
<div class="photo" style="left:956px;top:2243px;width:244px;height:242px;background:linear-gradient(135deg,#4e5a6c 0%,#7b8290 45%,#2d3646 80%,#c7c9cc 100%)" role="img" aria-label="Two colleagues reviewing documents at a table"></div>

<!-- team -->
<section class="team-band" role="img" aria-label="Team meeting around a table, tinted navy"></section>
<h2 class="abs center-heading" style="top:3026px;color:var(--white);font-size:32px;z-index:2">Meet Our Team</h2>
<p class="abs center-copy" style="top:3091px;color:#e8ecf4;z-index:2;font-size:14px;line-height:24px">Lorem ipsum dolor sit amet, consectetur adipiscing elit, sed do eiusmod tempor<br>incididunt ut labore et dolore magna aliqua. Quis ipsum suspendisse ultrices gravida.<br>Risus commodo viverra maecenas accumsan lacus vel facilisis.</p>

<!-- portfolio -->
<div class="photo" style="left:103px;top:3408px;width:583px;height:421px;background:linear-gradient(135deg,#d8d6d0 0%,#b9a38a 40%,#5e5550 70%,#2a2a2e 100%)" role="img" aria-label="Advisor reviewing papers with an older couple at a desk"></div>
<div class="abs eyebrow" style="left:731px;top:3491px">Gallery</div>
<h2 class="abs section-heading" style="left:731px;top:3527px">Portfolio Highlight</h2>
<p class="abs body-copy" style="left:731px;top:3590px;width:350px;color:var(--muted)">Lorem ipsum dolor sit amet, consectetur adip iscing elit, sed do eiusmod tempor incididunt ut labore et dolore magna aliqmod tempor incididunt ut labore et dolore mua.</p>
<a class="abs" style="left:731px;top:3716px;font-size:14px;font-weight:600;color:var(--ink)">Read More
  <svg width="26" height="12" viewBox="0 0 26 12" style="vertical-align:middle;margin-left:6px" fill="none" stroke="#0f1d3d" stroke-width="2" stroke-linecap="round"><path d="M1 6 H24 M19 1 L24 6 L19 11"/></svg></a>

<!-- news -->
<section class="news">
  <div class="abs eyebrow" style="left:0;top:76px;width:1200px;text-align:center">News</div>
  <h2 class="center-heading" style="top:111px">Latest News &amp; Insights</h2>
  <svg class="abs" style="left:72px;top:285px" width="36" height="16" viewBox="0 0 36 16" fill="none" stroke="#9aa0ab" stroke-width="2" stroke-linecap="round"><path d="M35 8 H2 M9 1 L2 8 L9 15"/></svg>
  <svg class="abs" style="left:1086px;top:285px" width="36" height="16" viewBox="0 0 36 16" fill="none" stroke="#0f1d3d" stroke-width="2" stroke-linecap="round"><path d="M1 8 H34 M27 1 L34 8 L27 15"/></svg>

  <article class="news-card" style="left:128px">
    <div class="photo" style="background:linear-gradient(135deg,#6b5a4a,#c4c8cf 50%,#e8eaee)" role="img" aria-label="Hands reviewing financial charts on paper"></div>
    <h3 class="news-title">Lorem ipsum dolor sitam consectetur ads.</h3>
    <p class="news-copy">Lorem ipsum dolor sit amecse ctetur adipiscing elit, sed dius mod tempor incididun.</p>
  </article>
  <article class="news-card" style="left:454px">
    <div class="photo" style="background:linear-gradient(135deg,#3d4656,#6d7280 50%,#2b2f38)" role="img" aria-label="Businesswoman presenting in a meeting"></div>
    <h3 class="news-title">Lorem ipsum dolor sitam consectetur ads.</h3>
    <p class="news-copy">Lorem ipsum dolor sit amecse ctetur adipiscing elit, sed dius mod tempor incididun.</p>
  </article>
  <article class="news-card" style="left:777px">
    <div class="photo" style="background:linear-gradient(135deg,#4a4e58,#8c8f96 45%,#d8dade)" role="img" aria-label="Businesswoman listening in a discussion"></div>
    <h3 class="news-title">Lorem ipsum dolor sitam consectetur ads.</h3>
    <p class="news-copy">Lorem ipsum dolor sit amecse ctetur adipiscing elit, sed dius mod tempor incididun.</p>
  </article>
</section>

<!-- footer -->
<footer class="site-footer">
  <div class="footer-brand">VARNEL RIDGE HOLDINGS</div>
  <p class="footer-copy">Lorem ipsum dolor sit amet, consectetur adipiscing elit, sed do eiusmod tempor incididunt ut labore et dolore magna aliqua.</p>
  <ul class="footer-links" style="left:779px"><li>Home</li><li>About Us</li><li>Team</li><li>Portfolio</li><li>Contact Us</li></ul>
  <ul class="footer-links" style="left:979px"><li>Privacy</li><li>Terms</li><li>Site Map</li></ul>
  <div class="footer-rule"></div>
  <p class="copyright">Copyright © 2025 All Rights Are Reserved.</p>
  <span class="social-dot"></span>
</footer>

</body>
</html>
```